Architectural, Engineering and Design Build

Tavonex4.com
Veteran Disabled Certified company is doing business in Architecture, Engineer and Design build - look simialr websites and come up with design follow following website
https://dorsey-kalbin.example/
https://www.velmonteam.example/
https://www.pirnoqa.example/contract-vehicles/service-disabled-veteran-owned-small-business-sdvosb/
https://www.corbelhubnet.example/about/sdvosb/

Target Market(s)

US - Defense and Federal Government

Industry/Entity Type

Colors
0054AA
0677BA
7BADD7
CADEEF
E8F1F8

Requirements
Must have
• Army, American patriotism , Buildings, construction, architecture, engineering
Nice to have
• I need to attract federal government agencies and Defense

```html
<!DOCTYPE html>
<html lang="en">
<head>
<meta charset="utf-8">
<title>Architecture, Engineering and Design Build</title>
<link href="https://fonts.googleapis.com/css2?family=Source+Sans+3:wght@400;600;700&display=swap" rel="stylesheet">
<style>
:root{
  --brand:#0054AA;
  --brand-mid:#0677BA;
  --brand-soft:#7BADD7;
  --brand-pale:#CADEEF;
  --brand-mist:#E8F1F8;
  --ink:#2e2e2e;
  --muted:#555;
  --page:#f2f2f2;
  --white:#fff;
  --footer:#1b1b1b;
  --star:#f5c518;
}
*{box-sizing:border-box;margin:0;padding:0}
html,body{width:1200px;height:3436px;overflow:hidden}
body{position:relative;font-family:"Source Sans 3",sans-serif;color:var(--ink);background:var(--white)}
.abs{position:absolute}
a{color:inherit;text-decoration:none}

/* hero */
.hero{left:0;top:0;width:1200px;height:722px;
  background:linear-gradient(100deg,#1d2f52 0%,#2b4670 40%,#4d5e78 70%,#6d7684 100%)}
.hero-shade{left:0;top:0;width:1200px;height:722px;background:linear-gradient(180deg,rgba(10,25,60,.55),rgba(10,25,60,.15) 60%,rgba(40,40,50,.25))}
.brand-mark{left:125px;top:30px;font-size:60px;font-weight:700;letter-spacing:6px;color:var(--white);line-height:1}
.main-nav{right:53px;top:55px;display:flex;gap:38px;font-weight:700;font-size:18px;color:var(--white)}
.hero-title{left:0;width:1200px;top:288px;text-align:center;color:var(--white);font-size:37px;font-weight:700;line-height:58px}
.btn-ghost{display:flex;align-items:center;justify-content:center;border:2px solid var(--white);border-radius:3px;color:var(--white);font-weight:700;font-size:17px}
.hero-btn{left:508px;top:431px;width:187px;height:51px}

/* intro */
.intro-title{left:0;width:1200px;top:772px;text-align:center;font-size:36px;font-weight:600;line-height:49px;color:var(--ink)}
.btn-outline{display:flex;align-items:center;justify-content:center;border:2px solid var(--brand);border-radius:3px;color:var(--brand);font-weight:700;font-size:19px;background:var(--white)}
.intro-btn{left:467px;top:898px;width:296px;height:45px}

.service-card{top:998px;width:510px;height:324px;background:var(--white);box-shadow:0 2px 12px rgba(0,0,0,.08);display:flex}
.service-photo{width:227px;height:324px}
.service-body{padding:34px 0 0 32px;width:283px}
.service-body svg{display:block;margin-bottom:20px}
.service-body h3{font-size:19px;font-weight:600;margin-bottom:14px}
.service-body p{font-size:13.5px;line-height:20px;color:var(--muted);width:220px}
.btn-solid{display:inline-flex;align-items:center;justify-content:center;background:var(--brand);color:var(--white);font-size:12.5px;font-weight:600;width:111px;height:37px;margin-top:26px}

/* projects */
.projects-band{left:0;top:1417px;width:1200px;height:455px;background:var(--brand)}
.projects-lower{left:0;top:1872px;width:1200px;height:884px;background:var(--page)}
.ghost-word{left:50px;top:1462px;font-size:190px;font-weight:700;letter-spacing:30px;color:transparent;-webkit-text-stroke:1px rgba(255,255,255,.12);line-height:1}
.eyebrow-light{left:88px;top:1510px;font-size:22px;font-weight:700;color:var(--white)}
.projects-title{left:53px;top:1542px;font-size:42px;font-weight:700;line-height:59px;color:var(--white)}
.projects-copy{left:504px;top:1553px;width:660px;font-size:17px;line-height:28px;color:var(--white)}
.project-tile{top:1733px;width:209px;height:265px}
.tile-caption{position:absolute;left:18px;bottom:22px;color:var(--white);font-size:13px;font-weight:700;line-height:28px}
.tile-caption span{display:block;border-left:3px solid #e53935;padding-left:8px}
.more-btn{left:546px;top:2039px;width:166px;height:45px;font-size:17px}

/* testimonials */
.map-glow{left:150px;top:2180px;width:920px;height:240px;background:radial-gradient(ellipse at center,rgba(200,200,200,.45),rgba(242,242,242,0) 70%)}
.eyebrow-blue{left:0;width:1200px;top:2218px;text-align:center;font-size:25px;font-weight:700;color:var(--brand)}
.testimonial-title{left:0;width:1200px;top:2262px;text-align:center;font-size:37px;font-weight:600;color:var(--ink)}
.testimonial-title b{color:var(--brand)}
.quote-card{top:2402px;width:465px;height:235px;background:var(--white);box-shadow:0 2px 14px rgba(0,0,0,.08)}
.avatar{position:absolute;left:30px;top:30px;width:94px;height:94px;border-radius:50%}
.quote-text{position:absolute;left:154px;top:30px;width:268px;font-size:13.5px;line-height:23px;color:var(--muted)}
.quote-name{position:absolute;left:154px;top:136px;font-size:18px;font-weight:600}
.stars{position:absolute;left:154px;top:174px;display:flex;gap:3px}
.quote-mark{position:absolute;right:32px;top:154px}
.slider-arrow{width:50px;height:50px;border-radius:50%;background:var(--white);box-shadow:0 2px 10px rgba(0,0,0,.1);display:flex;align-items:center;justify-content:center}

/* cta */
.cta-band{left:0;top:2756px;width:1200px;height:334px;background:linear-gradient(90deg,#6b4a22 0%,#b07a2e 30%,#7a5a36 55%,#4e3f36 80%,#6a3a2a 100%)}
.cta-shade{left:0;top:2756px;width:1200px;height:334px;background:rgba(20,15,10,.35)}
.cta-title{left:0;width:1200px;top:2818px;text-align:center;color:var(--white);font-size:38px;font-weight:700;line-height:55px}
.cta-btn{left:530px;top:2962px;width:184px;height:54px;font-size:21px}

/* footer */
.site-footer{left:0;top:3090px;width:1200px;height:346px;background:linear-gradient(180deg,#2a2a2a,#121212)}
.footer-nav{left:0;width:1200px;top:3145px;display:flex;justify-content:center;gap:18px;color:var(--white);font-size:16px}
.footer-nav .sep{opacity:.8}
.footer-mark{left:53px;top:3228px;font-size:60px;font-weight:400;color:#5a5a5a;line-height:1}
.social{top:3226px;width:60px;height:60px;border:2px solid #bdbdbd;border-radius:50%}
.copyright{left:0;width:1200px;top:3374px;text-align:center;font-size:14px;color:#bdbdbd}
</style>
</head>
<body>

<!-- hero -->
<div class="abs hero" role="img" aria-label="Photo of a capitol dome with a national flag on a flagpole against blue sky"></div>
<div class="abs hero-shade"></div>
<div class="abs brand-mark">LOGO</div>
<nav class="abs main-nav"><a href="#">ABOUT</a><a href="#">SERVICES</a><a href="#">PROJECTS</a><a href="#">CONTACT US</a></nav>
<h1 class="abs hero-title">Veteran Disabled Certified Company<br>Owned Business</h1>
<a class="abs btn-ghost hero-btn" href="#">GET STARTED NOW</a>

<!-- intro -->
<h2 class="abs intro-title">Technology to take products from<br>an idea all the way to the end consumer.</h2>
<a class="abs btn-outline intro-btn" href="#">BOOK A CONSULTATION</a>

<article class="abs service-card" style="left:50px">
  <div class="service-photo" role="img" aria-label="Glass pavilion building beside water" style="background:linear-gradient(160deg,#c9d3dc,#6f7f8c 50%,#3c4a3a)"></div>
  <div class="service-body">
    <svg width="60" height="64" viewBox="0 0 60 64" fill="none" stroke="#0054AA" stroke-width="2"><path d="M12 22a18 18 0 0 1 36 0z"/><path d="M8 22h44"/><path d="M16 24a14 14 0 0 0 28 0"/><path d="M4 62V52a10 10 0 0 1 10-10h32a10 10 0 0 1 10 10v10"/><path d="M22 42v20M38 42v20M30 6v8"/></svg>
    <h3>Construction</h3>
    <p>Donec scelerisque dolor id nunc dictum, interdum gravida mauris rhoncus. Aliquam</p>
    <a class="btn-solid" href="#">GET STARTED</a>
  </div>
</article>
<article class="abs service-card" style="left:641px">
  <div class="service-photo" role="img" aria-label="Glass office tower seen from below against blue sky" style="background:linear-gradient(160deg,#a9c8e6,#2b5a8a 50%,#123456)"></div>
  <div class="service-body">
    <svg width="66" height="64" viewBox="0 0 66 64" fill="none" stroke="#0054AA" stroke-width="2"><path d="M4 14h40v44H4z"/><path d="M4 14c0-6 8-6 8 0v44"/><path d="M44 30h18v28H44"/><circle cx="42" cy="8" r="4"/><path d="M42 12l-8 30M42 12l8 30M36 30h12"/></svg>
    <h3>Architecture</h3>
    <p>Donec scelerisque dolor id nunc dictum, interdum gravida mauris rhoncus. Aliquam</p>
    <a class="btn-solid" href="#">GET STARTED</a>
  </div>
</article>

<!-- projects -->
<div class="abs projects-band"></div>
<div class="abs projects-lower"></div>
<div class="abs ghost-word">PROJECTS</div>
<div class="abs eyebrow-light">LATEST PROJECTS</div>
<h2 class="abs projects-title">Let’s Explore Our<br>Recent Works</h2>
<p class="abs projects-copy">The right software solution by itself will not run your business. It takes a team to do that. In addition to selecting the best cloud solution on the market, it takes smart and dedicated people remaining essentially unchanged.</p>

<div class="abs project-tile" style="left:245px;background:linear-gradient(180deg,#1f3c52,#4a4d8a 55%,#1a1f3a)" role="img" aria-label="City skyline at dusk">
  <div class="tile-caption">Commercial &nbsp;Residential<span>Modern House</span></div>
</div>
<div class="abs project-tile" style="left:474px;background:linear-gradient(180deg,#2a6ab0,#7fa8d0 55%,#c9a45a 75%,#4d6a8a)" role="img" aria-label="Curved modern cultural centre building lit at dusk"></div>
<div class="abs project-tile" style="left:710px;background:linear-gradient(180deg,#d7e4ee,#a9b98a 45%,#3f6a5a 75%,#2c3d34)" role="img" aria-label="Building under construction with tower crane"></div>
<div class="abs project-tile" style="left:940px;background:linear-gradient(180deg,#f2f2f2,#d2d2d2 50%,#b8b8b8)" role="img" aria-label="Architectural scale model of a building on plans"></div>

<a class="abs btn-outline more-btn" href="#">VIEW MORE</a>

<!-- testimonials -->
<div class="abs map-glow" role="img" aria-label="Faint dotted world map"></div>
<div class="abs eyebrow-blue">TESTIMONIALS</div>
<h2 class="abs testimonial-title">Words From <b>Clients</b></h2>

<article class="abs quote-card" style="left:121px">
  <div class="avatar" role="img" aria-label="Client portrait" style="background:linear-gradient(160deg,#c7d3da,#7a8b96)"></div>
  <p class="quote-text">when an unknown printer took a galley of type and scrambled it to make a type not only five centurie when an unknown printer took a galley of type</p>
  <div class="quote-name">Ravel Tosmin</div>
  <div class="stars"><svg width="70" height="12" viewBox="0 0 70 12"><g fill="#f5c518"><path id="st" d="M6 0l1.8 3.9 4.2.4-3.2 2.8 1 4.1L6 9 2.2 11.2l1-4.1L0 4.3l4.2-.4z"/><use href="#st" x="14"/><use href="#st" x="28"/><use href="#st" x="42"/></g><use href="#st" x="56" fill="#999"/></svg></div>
  <svg class="quote-mark" width="42" height="36" viewBox="0 0 42 36" fill="#7BADD7"><path d="M0 0h18v20l-8 16H2l6-14H0zM24 0h18v20l-8 16h-8l6-14h-8z"/></svg>
</article>
<article class="abs quote-card" style="left:621px">
  <div class="avatar" role="img" aria-label="Client portrait" style="background:linear-gradient(160deg,#3d7fb0,#1e3346)"></div>
  <p class="quote-text">when an unknown printer took a galley of type and scrambled it to make a type not only five centurie when an unknown printer took a galley of type</p>
  <div class="quote-name">Kiran Delbrook</div>
  <div class="stars"><svg width="70" height="12" viewBox="0 0 70 12"><g fill="#f5c518"><use href="#st"/><use href="#st" x="14"/><use href="#st" x="28"/><use href="#st" x="42"/></g><use href="#st" x="56" fill="#999"/></svg></div>
  <svg class="quote-mark" width="42" height="36" viewBox="0 0 42 36" fill="#7BADD7"><path d="M0 0h18v20l-8 16H2l6-14H0zM24 0h18v20l-8 16h-8l6-14h-8z"/></svg>
</article>
<div class="abs slider-arrow" style="left:52px;top:2496px"><svg width="10" height="14" viewBox="0 0 10 14" fill="none" stroke="#333" stroke-width="1.5"><path d="M7 2L2 7l5 5"/></svg></div>
<div class="abs slider-arrow" style="left:1101px;top:2492px"><svg width="10" height="14" viewBox="0 0 10 14" fill="none" stroke="#333" stroke-width="1.5"><path d="M3 2l5 5-5 5"/></svg></div>

<!-- call to action -->
<div class="abs cta-band" role="img" aria-label="City skyline at sunset with warm golden light"></div>
<div class="abs cta-shade"></div>
<h2 class="abs cta-title">Please feel free to contact us if you have any<br>question or queries</h2>
<a class="abs btn-ghost cta-btn" href="#">CONTACT US</a>

<!-- footer -->
<footer class="abs site-footer"></footer>
<nav class="abs footer-nav">
  <a href="#">Home</a><span class="sep">|</span><a href="#">Services</a><span class="sep">|</span><a href="#">Services</a><span class="sep">|</span><a href="#">Contact</a><span class="sep">|</span><a href="#">About</a><span class="sep">|</span><a href="#">Blog</a>
</nav>
<div class="abs footer-mark">LOGO</div>
<a class="abs social" style="left:661px" href="#" aria-label="Social profile 1"></a>
<a class="abs social" style="left:738px" href="#" aria-label="Social profile 2"></a>
<a class="abs social" style="left:817px" href="#" aria-label="Social profile 3"></a>
<a class="abs social" style="left:893px" href="#" aria-label="Social profile 4"></a>
<a class="abs social" style="left:973px" href="#" aria-label="Social profile 5"></a>
<div class="abs copyright">Copyright © 2024. All Rights Reserved.</div>

</body>
</html>
```